Modern Web Design for Nonprofit Organization

Our client is looking to redesign their website. They want a modern look, clean and professional, that integrates their new brand guidelines.

Here is clients current site:
http://www.brontalvo.org/

They want their own unique design but here are some sites the clients likes:
https://www.pelorvane.com/en/
https://kelmoraswift.org/
https://www.dunbrook.com/
https://www.tovikstad.com/
https://www.quellmarren.org/

Attached please find the clients logos, color palette, site plan and design specs.

You will create a homepage mockup that will have the following sections in this order:
1. Thin Alert Bar at very top with one line message
2. Nav Bar with Logo and Main Nav (red in site plan)
3. Hero Image or Video
4. Signup Bar with name email and zip and connect button
5. Intro section with image, welcome message, and supporter counter
6. Featured Action section with call to action
7. Event section with two upcoming event cards
8. Latest News section with three latest blog post
9. Support our work (donation) section
10. Worker and Member Stories Section with feed of social posts
11. Footer.

You can use text and images from clients existing site or placeholder images and placeholder text.

Please submit as many home page mockups/idea boards as you like. Client will pick the top three and ask for some revisions. If you are selected this will lead to a lot of work for this client.

Project is private please adhere to PlanoHarbor terms of use and do not share any materials please.

QUICKEST RESPONSE PLEASE!

Thanks for looking!

Non profit donors and farmworker advocates

2 page

Sans Serif

• Adhere to brief and client brand ID
• World class design

```html
<!DOCTYPE html>
<html lang="es">
<head>
<meta charset="utf-8">
<title>Campo Unido Foundation</title>
<link href="https://fonts.googleapis.com/css2?family=Nunito:wght@700;800;900&family=Lato:wght@400;700&family=Raleway:wght@400&display=swap" rel="stylesheet">
<style>
:root{
  --yellow:#FFCC00;
  --red:#D50000;
  --black:#000;
  --white:#fff;
  --grey:#F0F0F0;
  --teal:#00959A;
  --text:#222;
  --cream:#FFF3C4;
}
*{margin:0;padding:0;box-sizing:border-box}
html,body{width:1200px;height:3460px;overflow:hidden}
body{position:relative;font-family:'Lato',sans-serif;color:var(--text);background:var(--white)}
.abs{position:absolute}
.alert-bar{left:0;top:0;width:1200px;height:42px;background:var(--yellow);font-size:15px;display:flex;align-items:center;justify-content:space-between;padding:0 30px 0 33px}
.alert-bar .dots{display:flex;gap:22px}
.alert-bar .dots span{width:20px;height:20px;background:var(--black);border-radius:50%}
.nav{left:0;top:42px;width:1200px;height:83px;background:var(--red)}
.brand{left:33px;top:0;width:259px;height:83px;background:var(--white);display:flex;align-items:center;padding-left:16px;gap:12px}
.brand .mark{width:40px;height:40px;border-radius:50%;background:var(--red)}
.brand .name{font-family:'Nunito',sans-serif;font-weight:800;font-size:19px;line-height:21px;color:var(--black)}
.menu{right:32px;top:0;height:83px;display:flex;align-items:center;gap:21px;color:var(--white);font-size:17px;font-weight:700}
.hero{left:0;top:125px;width:1200px;height:468px;background:linear-gradient(120deg,#7a5a48,#b2483d 35%,#3d4a6b 70%,#8c8f9e)}
.hero h1{position:absolute;left:33px;top:325px;font-family:'Nunito',sans-serif;font-weight:800;font-size:58px;color:var(--yellow)}
.btn{display:flex;align-items:center;justify-content:center;font-size:17px}
.hero .btn{position:absolute;left:960px;top:329px;width:206px;height:73px;background:var(--black);color:var(--white);border:2px solid var(--white);border-radius:8px}
.welcome{left:0;top:593px;width:1200px;height:493px;background:var(--grey)}
.welcome h2{position:absolute;left:33px;top:85px;font-family:'Nunito',sans-serif;font-weight:800;font-size:38px;color:var(--black)}
.accent{color:var(--red)}
.welcome p{position:absolute;left:33px;top:226px;width:520px;font-family:'Raleway',sans-serif;font-size:28px;line-height:33px;color:#444}
.welcome .photo{position:absolute;left:609px;top:33px;width:591px;height:425px;background:linear-gradient(135deg,#3a3430,#8a6b4d 50%,#c9c3bb)}
.section-title{left:0;width:1200px;text-align:center;font-family:'Nunito',sans-serif;font-weight:800;font-size:31px;color:var(--black)}
.event{width:438px;color:var(--white)}
.event .body{padding:34px 32px 0;height:344px}
.event h3{font-family:'Nunito',sans-serif;font-weight:800;font-size:31px;margin-bottom:10px}
.event p{font-size:23px;line-height:43px}
.event ul{list-style:none;margin-top:20px;font-size:13px;position:relative}
.event li{line-height:36px}
.event li::before{content:"";display:inline-block;width:5px;height:5px;border:1px solid var(--white);border-radius:50%;margin-right:5px;vertical-align:middle}
.event .detail{position:absolute;right:0;bottom:2px;width:112px;height:28px;background:var(--yellow);color:var(--white);border-radius:5px;font-size:14px}
.event .photo{height:231px}
.quote-band{left:0;top:1789px;width:1200px;height:166px;background:var(--teal)}
.quote-mark{font-family:'Nunito',sans-serif;font-weight:900;font-size:150px;line-height:1;color:rgba(255,255,255,.55)}
.quote-band .quote-mark{position:absolute;left:116px;top:-4px}
.quote-band p{position:absolute;left:202px;top:34px;font-family:'Nunito',sans-serif;font-weight:800;font-size:31px;line-height:46px;color:var(--white)}
.yellow-btn{background:var(--yellow);color:var(--black);border-radius:8px;box-shadow:0 3px 6px rgba(0,0,0,.25)}
.quote-band .btn{position:absolute;left:868px;top:47px;width:207px;height:72px}
.news{top:2037px;width:378px;height:476px;background:var(--white);box-shadow:0 0 6px rgba(0,0,0,.25);border-radius:6px;overflow:hidden}
.news h4{position:absolute;left:31px;top:27px;color:var(--red);font-size:14px;font-weight:700}
.news p{position:absolute;left:31px;top:54px;width:320px;font-size:10.5px;line-height:17.5px}
.news .btn{position:absolute;left:74px;top:234px;width:208px;height:74px}
.news .photo{position:absolute;left:0;top:348px;width:378px;height:128px;background:linear-gradient(180deg,#8a5a3a,#3b2b25 55%,#6a4e3e)}
.stories{left:0;top:2596px;width:1200px;height:409px;background:linear-gradient(120deg,#2b2f3a,#5d4c48 50%,#2c3240)}
.story-card{left:83px;top:2638px;width:1032px;height:324px;background:var(--white);border-radius:8px}
.story-card .quote-mark{position:absolute;left:30px;top:0;color:#777}
.story-card p{position:absolute;left:104px;top:44px;font-family:'Nunito',sans-serif;font-weight:800;font-size:30px;line-height:46px;color:#222}
.avatar{position:absolute;left:823px;top:161px;width:140px;height:140px;border-radius:50%;background:linear-gradient(180deg,#e9d8c4,#b7c9d8);border:1px solid #555}
.signup{left:0;top:3005px;width:1200px;height:167px;background:var(--yellow)}
.signup .field{position:absolute;left:117px;top:47px;width:715px;height:72px;background:var(--cream);border-radius:8px;padding-left:16px;display:flex;align-items:center;font-size:25px;color:#888}
.signup .btn{position:absolute;left:868px;top:47px;width:207px;height:72px;background:var(--red);color:var(--white);border-radius:8px;font-size:25px;box-shadow:0 3px 6px rgba(0,0,0,.25)}
.footer{left:0;top:3172px;width:1200px;height:239px;background:var(--black);color:var(--white);font-size:18px}
.col{position:absolute;top:36px}
.col h5{font-size:18px;font-weight:400;margin-bottom:26px}
.col h5.strong{font-weight:700}
.col li{list-style:none;height:41px;display:flex;align-items:center;gap:14px}
.col svg{width:24px;height:24px}
.legal{left:0;top:3411px;width:1200px;height:49px;background:var(--red);color:var(--white);font-size:18px;display:flex;align-items:center;padding-left:130px;gap:56px}
</style>
</head>
<body>

<div class="abs alert-bar">
  <span>One Line Message</span>
  <div class="dots"><span></span><span></span><span></span><span></span><span></span></div>
</div>

<header class="abs nav">
  <div class="abs brand"><span class="mark"></span><span class="name">CAMPO UNIDO<br>FOUNDATION</span></div>
  <nav class="abs menu">
    <svg width="34" height="28" viewBox="0 0 34 28"><path d="M17 2 2 15h4v11h8v-7h6v7h8V15h4z" fill="#fff"/></svg>
    <span>GET HELP NOW</span><span>TAKE ACTION</span><span>NEWS AND EVENTS</span><span>SUPPORT OUR WORK</span><span>ABOUT US</span>
  </nav>
</header>

<section class="abs hero" role="img" aria-label="Photo of supporters marching with banners and placards">
  <h1>Unete A La Lucha!</h1>
  <div class="btn">DONATION</div>
</section>

<section class="abs welcome">
  <h2>Welcome <span class="accent">Message</span></h2>
  <p>La CUF nunca le cobrara por los mensajes por texto pero su compañía de teléfono puede aplicarle cargos de acuerdo a su plan</p>
  <div class="photo" role="img" aria-label="Photo of people working with a laptop at a wooden table with drinks"></div>
</section>

<h2 class="abs section-title" style="top:1113px">Upcoming <span class="accent">Event</span></h2>

<article class="abs event" style="left:124px;top:1179px;background:var(--red)">
  <div class="body">
    <h3>Centro de Recursos</h3>
    <p>Sell in-store, at retail events, pop-up stores and even online. With all sales channels in one POS software, Tillo</p>
    <ul><li>Sell in-store</li><li>Sell on-the-go</li><div class="detail btn">Event Detail</div></ul>
  </div>
  <div class="photo" role="img" aria-label="Photo of volunteers at an outdoor resource table" style="background:linear-gradient(135deg,#5a6a72,#c8c8c8 50%,#a52a2a)"></div>
</article>

<article class="abs event" style="left:638px;top:1179px;background:var(--black)">
  <div class="body" style="height:340px">
    <h3>Comparte Tu Historia</h3>
    <p>Sell in-store, at retail events, pop-up stores and even online. With all sales channels in one POS software, Tillo</p>
    <ul><li>Sell in-store</li><li>Sell on-the-go</li><div class="detail btn">Event Detail</div></ul>
  </div>
  <div class="photo" role="img" aria-label="Photo of farmworkers holding red flags in a vineyard" style="height:235px;background:linear-gradient(135deg,#2f5a1e,#6b9a3a 50%,#3c6a2a)"></div>
</article>

<section class="abs quote-band">
  <span class="quote-mark">“</span>
  <p>Remember that the happiest people are not<br>those getting more, but those giving more.</p>
  <div class="btn yellow-btn">DONATION</div>
</section>

<h2 class="abs section-title" style="top:1981px">Latest <span class="accent">News</span></h2>

<article class="abs news" style="left:16px">
  <h4>Participacion Civica</h4>
  <p>Nuestro departamento de póliza y participacion civica está comprometido a mantener el esfuerzo colectivo para mejorar las vidas de nuestras comunidades.Nuestro departamento firmemente cree que todas las personas tienen algo que contribuir en la lucha para un mejor futuro. Por Media de esfuerzos organizativos a nivel local, estatal, nacional y mundial creamos empoderamiento en nuestras comunidades el cual se refleja en las vidas de aquellos que desean dejarle a sus hijos un mundo mejor.</p>
  <div class="btn yellow-btn">MORE INFO</div>
  <div class="photo" role="img" aria-label="Photo of an audience seated at a community meeting"></div>
</article>
<article class="abs news" style="left:410px">
  <h4>Participacion Civica</h4>
  <p>Nuestro departamento de póliza y participacion civica está comprometido a mantener el esfuerzo colectivo para mejorar las vidas de nuestras comunidades.Nuestro departamento firmemente cree que todas las personas tienen algo que contribuir en la lucha para un mejor futuro. Por Media de esfuerzos organizativos a nivel local, estatal, nacional y mundial creamos empoderamiento en nuestras comunidades el cual se refleja en las vidas de aquellos que desean dejarle a sus hijos un mundo mejor.</p>
  <div class="btn yellow-btn">MORE INFO</div>
  <div class="photo" role="img" aria-label="Photo of an audience seated at a community meeting"></div>
</article>
<article class="abs news" style="left:804px">
  <h4>Participacion Civica</h4>
  <p>Nuestro departamento de póliza y participacion civica está comprometido a mantener el esfuerzo colectivo para mejorar las vidas de nuestras comunidades.Nuestro departamento firmemente cree que todas las personas tienen algo que contribuir en la lucha para un mejor futuro. Por Media de esfuerzos organizativos a nivel local, estatal, nacional y mundial creamos empoderamiento en nuestras comunidades el cual se refleja en las vidas de aquellos que desean dejarle a sus hijos un mundo mejor.</p>
  <div class="btn yellow-btn">MORE INFO</div>
  <div class="photo" role="img" aria-label="Photo of an audience seated at a community meeting"></div>
</article>

<h2 class="abs section-title" style="top:2539px">Member <span class="accent">Stories</span></h2>

<section class="abs stories" role="img" aria-label="Dim photo of a rally crowd behind the member story"></section>
<article class="abs story-card">
  <span class="quote-mark">“</span>
  <p>Como miembro, tendra su voz como parte de los cientos de<br>voces que forman parte de la lucha por la reforma migratoria.</p>
  <div class="avatar" role="img" aria-label="Portrait photo of a smiling member"></div>
</article>

<section class="abs signup">
  <div class="field">Enter email to signup</div>
  <div class="btn">SIGNUP</div>
</section>

<footer class="abs footer">
  <div class="col" style="left:128px">
    <h5>Contact Us</h5>
    <ul>
      <li><svg viewBox="0 0 24 24"><circle cx="12" cy="12" r="9" fill="none" stroke="#fff" stroke-width="1.5"/><path d="M8 7c0 5 4 9 9 9l1-2-3-1-1 1c-2-1-3-2-4-4l1-1-1-3z" fill="#fff"/></svg>1-800-555-0142</li>
      <li><svg viewBox="0 0 24 24"><path d="M12 3a6 6 0 0 0-6 6c0 5 6 12 6 12s6-7 6-12a6 6 0 0 0-6-6z" fill="none" stroke="#fff" stroke-width="1.5"/><circle cx="12" cy="9" r="2" fill="#fff"/></svg>Address</li>
      <li><svg viewBox="0 0 24 24"><rect x="3" y="6" width="18" height="12" fill="none" stroke="#fff" stroke-width="1.5"/><path d="M3 6l9 7 9-7" fill="none" stroke="#fff" stroke-width="1.5"/></svg>info@brontalvo.com</li>
    </ul>
  </div>
  <div class="col" style="left:505px">
    <h5>Our Company</h5>
    <ul><li>About</li><li>About us</li><li>Blog</li></ul>
  </div>
  <div class="col" style="left:869px">
    <h5 class="strong">Social Contacts</h5>
    <ul>
      <li><svg viewBox="0 0 24 24"><circle cx="12" cy="12" r="8" fill="#fff"/></svg>Friendlink</li>
      <li><svg viewBox="0 0 24 24"><circle cx="12" cy="12" r="8" fill="#fff"/></svg>Snapframe</li>
      <li><svg viewBox="0 0 24 24"><circle cx="12" cy="12" r="8" fill="#fff"/></svg>Vidstream</li>
      <li><svg viewBox="0 0 24 24"><circle cx="12" cy="12" r="8" fill="#fff"/></svg>Chirper</li>
    </ul>
  </div>
</footer>

<div class="abs legal"><span>Privacy Policy</span><span>Terms and Conditions</span></div>

</body>
</html>
```